Business Card Design Project For Moving Company

Hello,

We need the business card to be 2 sided and we were thinking to use the logo on the front of the card (see file 1 attached) and the text "logo" (see file 2 attached) in the back of the card. We're looking for a powerful design that will help us build our brand, as our company is new.
We are a full service moving company (no storage) located in San Diego, CA, USA. The design should communicate to our potential customers that we have the highest level of service, customer satisfaction is our number one goal, our team is professional and efficient.

Thank you,

Gil
Updates

Project Deadline Extended
Reason: We would like to have more time to provide feedback for the designs already submitted. Thank you, Gil

Industry/Entity Type

Moving Company

Requirements
Must have
• Front of the card must have the following text and logo:
Haul Brightway, Inc
Residential And Commercial
Local And Long Distance
Address: 3917 Alder Crest Rd, #412,
San Diego, CA, 92087
P: 855-372-LIFT (5438)
F: 858-291-4476
info@haul-brightway.com
www.haul-brightway.com

Back of the card must have the following text and text "logo" (file 2 attached):

The best compliment we can ever receive is a referral from our clients.

```html
<!DOCTYPE html>
<html lang="en">
<head>
<meta charset="utf-8">
<title>Haul Brightway – Business Card</title>
<link rel="stylesheet" href="https://fonts.googleapis.com/css2?family=Open+Sans:wght@400;600;700;800&display=swap">
<style>
  :root {
    --page: #2b2b2b;
    --card-white: #f7f7f7;
    --card-black: #1f1d1e;
    --band: #1c1b1b;
    --red: #d3151c;
    --ink: #2a2a2a;
    --grey: #5a5a5a;
    --mark-soft: #e9a48d;
    --silver: #b9b9b9;
  }
  * { margin: 0; padding: 0; box-sizing: border-box; }
  html, body { width: 1200px; height: 900px; overflow: hidden; }
  body {
    background: var(--page);
    font-family: "Open Sans", Arial, sans-serif;
    position: relative;
  }
  .card {
    position: absolute;
    left: 260px;
    width: 680px;
    height: 389px;
    overflow: hidden;
    box-shadow: 0 8px 24px rgba(0,0,0,.45);
  }
  /* Front */
  .card--front { top: 41px; background: var(--card-white); }
  .front-mark {
    position: absolute; left: 48px; top: 80px; width: 330px;
    display: flex; align-items: center; gap: 14px;
    color: var(--mark-soft); font-weight: 700; font-size: 44px; line-height: 1.1;
  }
  .front-mark .dot {
    flex: none; width: 34px; height: 34px; border-radius: 50%; background: var(--mark-soft);
  }
  .front-identity { position: absolute; left: 48px; top: 300px; color: var(--grey); }
  .front-identity .company { font-size: 22px; font-weight: 400; color: #4a4a4a; }
  .front-identity .service { font-size: 14px; font-weight: 600; line-height: 1.3; }
  .contact { position: absolute; left: 420px; top: 34px; list-style: none; }
  .contact li { margin-bottom: 8px; }
  .contact .label {
    display: block; color: var(--red); font-weight: 700; font-size: 13px;
    letter-spacing: .3px; line-height: 1.1;
  }
  .contact .value { display: block; color: var(--ink); font-size: 12px; line-height: 1.3; }
  .front-band { position: absolute; left: 0; top: 0; }
  .band-wordmark {
    position: absolute; right: 22px; top: 288px;
    color: var(--silver); font-weight: 800; font-size: 22px; line-height: 1;
    letter-spacing: .5px; text-transform: uppercase; white-space: nowrap;
  }
  /* Back */
  .card--back { top: 470px; background: var(--card-black); }
  .back-mark {
    position: absolute; left: 70px; top: 110px;
    display: flex; align-items: center; gap: 14px;
    color: var(--red); font-weight: 700; font-size: 44px; line-height: 1;
  }
  .back-mark .dot { flex: none; width: 34px; height: 34px; border-radius: 50%; background: var(--red); }
  .back-rule {
    position: absolute; right: 0; top: 58px; width: 110px; height: 2px; background: var(--red);
  }
  .tagline {
    position: absolute; left: 70px; top: 210px; width: 560px;
    color: #e6e6e6; font-size: 15px; font-weight: 400;
  }
</style>
</head>
<body>

<section class="card card--front" aria-label="Card front">
  <div class="front-mark"><span class="dot"></span><span class="mark-name">Haul<br>Brightway</span></div>

  <ul class="contact">
    <li><span class="label">ADDRESS</span><span class="value">3917 Alder Crest Rd, #412,<br>San Diego, CA, 92087</span></li>
    <li><span class="label">PHONE NO</span><span class="value">855-372-LIFT (5438)</span></li>
    <li><span class="label">FAX</span><span class="value">858-291-4476</span></li>
    <li><span class="label">EMAIL</span><span class="value">info@haul-brightway.com</span></li>
    <li><span class="label">WEB</span><span class="value">www.haul-brightway.com</span></li>
  </ul>

  <svg class="front-band" width="680" height="389" viewBox="0 0 680 389" aria-hidden="true">
    <polygon points="340,300 680,250 680,318 340,330" fill="var(--band)"/>
  </svg>
  <div class="band-wordmark">Haul Brightway</div>

  <div class="front-identity">
    <p class="company">Haul Brightway, Inc</p>
    <p class="service">Residential And Commercial<br>Local And Long Distance</p>
  </div>
</section>

<section class="card card--back" aria-label="Card back">
  <div class="back-rule"></div>
  <div class="back-mark"><span class="dot"></span><span class="mark-name">Haul Brightway</span></div>
  <p class="tagline">The best compliment we can ever receive is a referral from our clients.</p>
</section>

</body>
</html>
```